NEW YORK Plumbing/utility company 10 year anniversary business card

Looking For simple back and front business card would like to include a few things in description
We offer 24/7 emergency service
residential
commercial
industrial
municipal
services offered
Plumbing
hydro excavation
hydro jetting
Well pumps
Sewer pumps
water mains
sewer mains

```html
<!DOCTYPE html>
<html lang="en">
<head>
<meta charset="utf-8">
<title>Ridgeline Water &amp; Sewer – Business Card</title>
<link rel="stylesheet" href="https://fonts.googleapis.com/css2?family=Mulish:wght@400;700&display=swap">
<style>
  :root {
    --backdrop: #3a3e42;
    --card-white: #ffffff;
    --ink: #222222;
    --brand-blue: #1a7fc1;
    --panel-light: #2ac2e8;
    --panel-deep: #0277bf;
    --bullet: #2ac2e8;
    --text-on-panel: #ffffff;
  }
  * { box-sizing: border-box; margin: 0; padding: 0; }
  html, body {
    width: 1200px; height: 1000px; overflow: hidden;
    background: var(--backdrop);
    font-family: "Mulish", "Century Gothic", sans-serif;
  }
  .canvas { position: relative; width: 1200px; height: 1000px; }

  .card { position: absolute; }

  /* Front */
  .card-front {
    left: 126px; top: 88px; width: 702px; height: 386px;
    background: var(--card-white); color: var(--ink);
  }
  .brand {
    position: absolute; left: 64px; top: 232px; width: 240px;
    display: flex; align-items: center; gap: 10px;
    transform: translateY(-50%);
  }
  .brand-mark {
    width: 18px; height: 18px; border-radius: 50%;
    background: var(--brand-blue); flex: none;
  }
  .brand-name {
    color: var(--brand-blue); font-weight: 700;
    font-size: 22px; line-height: 1.2; letter-spacing: 0.5px;
  }
  .holder-name {
    position: absolute; left: 384px; top: 42px;
    font-size: 20px; letter-spacing: 0.5px;
  }
  .address {
    position: absolute; left: 384px; top: 124px;
    font-size: 18px; line-height: 23px;
  }
  .contact-list {
    position: absolute; left: 378px; top: 236px; list-style: none;
  }
  .contact-item {
    display: flex; align-items: center; gap: 14px;
    height: 40px; font-size: 18px;
  }
  .contact-icon { width: 26px; height: 26px; flex: none; }

  /* Back */
  .card-back {
    left: 386px; top: 528px; width: 712px; height: 392px;
    display: flex; color: var(--text-on-panel);
  }
  .panel-coverage {
    width: 352px; background: var(--panel-light);
    padding: 88px 0 0 73px; font-weight: 700; font-size: 23px; line-height: 32px;
  }
  .emergency { margin-bottom: 31px; }
  .sectors { list-style: none; }
  .panel-services {
    flex: 1; background: var(--panel-deep); padding: 56px 0 0 77px;
  }
  .services-title { font-weight: 700; font-size: 19px; margin-bottom: 38px; letter-spacing: 0.3px; }
  .services-list { list-style: none; margin-left: -20px; }
  .services-list li {
    font-size: 20px; line-height: 32px; display: flex; align-items: center; gap: 10px;
  }
  .services-list li::before {
    content: ""; width: 7px; height: 7px; border-radius: 50%; background: var(--bullet);
  }
</style>
</head>
<body>
<main class="canvas">
  <section class="card card-front" aria-label="Business card front">
    <div class="brand">
      <span class="brand-mark"></span>
      <span class="brand-name">Ridgeline Water &amp; Sewer</span>
    </div>
    <p class="holder-name">NAME</p>
    <p class="address">address, address, address<br>address, address, address</p>
    <ul class="contact-list">
      <li class="contact-item">
        <svg class="contact-icon" viewBox="0 0 24 24" aria-hidden="true"><path fill="#222" d="M6.6 10.8a15.1 15.1 0 0 0 6.6 6.6l2.2-2.2a1 1 0 0 1 1-.25 11.4 11.4 0 0 0 3.6.57 1 1 0 0 1 1 1V20a1 1 0 0 1-1 1A17 17 0 0 1 3 4a1 1 0 0 1 1-1h3.5a1 1 0 0 1 1 1c0 1.25.2 2.45.57 3.57a1 1 0 0 1-.25 1z"/></svg>
        <span>845-555-0182</span>
      </li>
      <li class="contact-item">
        <svg class="contact-icon" viewBox="0 0 24 24" aria-hidden="true"><rect x="2" y="5" width="20" height="14" fill="#222"/><path d="M3 6l9 7 9-7" fill="none" stroke="#fff" stroke-width="1.6"/></svg>
        <span>info@ridgelinews.com</span>
      </li>
      <li class="contact-item">
        <svg class="contact-icon" viewBox="0 0 24 24" aria-hidden="true" fill="none" stroke="#222" stroke-width="1.6"><circle cx="12" cy="12" r="10"/><ellipse cx="12" cy="12" rx="4.5" ry="10"/><path d="M2 12h20M4 7h16M4 17h16"/></svg>
        <span>www.</span>
      </li>
    </ul>
  </section>

  <section class="card card-back" aria-label="Business card back">
    <div class="panel-coverage">
      <p class="emergency">We offer 24/7<br>emergency service</p>
      <ul class="sectors">
        <li>Residential</li>
        <li>Commercial</li>
        <li>Industrial</li>
        <li>Municipal</li>
      </ul>
    </div>
    <div class="panel-services">
      <h2 class="services-title">SERVICES OFFERED</h2>
      <ul class="services-list">
        <li>Plumbing</li>
        <li>Hydro Excavation</li>
        <li>Hydro Jetting</li>
        <li>Well Pumps</li>
        <li>Sewer pumps</li>
        <li>Water Mains</li>
        <li>Sewer Mains</li>
      </ul>
    </div>
  </section>
</main>
</body>
</html>
```